Tolvin Waste Website Design

Our new start-up needs a website design. We plan to help businesses find more sustainable ways to manage their waste. Our initial website aims to gather contact data from potential business customers and comprehensive information from waste facilities and waste transporters. We have a logo design (attached) which we would like included in the website design. I have also attached a number of pages that describe what information should appear on each page as well as a web design brief file that describes the look we are after.

```html
<!DOCTYPE html>
<html lang="en">
<head>
<meta charset="utf-8">
<title>Tolvin Waste – Waste Transporters</title>
<link rel="stylesheet" href="https://fonts.googleapis.com/css2?family=Poppins:wght@400;500;600&family=Roboto:ital,wght@0,400;0,500;1,400&display=swap">
<style>
:root{
  --green:#5a9a2a;
  --green-light:#8cc63f;
  --white:#ffffff;
  --text-light:#e8e8e8;
  --input-bg:#ffffff;
  --placeholder:#8a8a8a;
  --field-text:#444444;
  --frame:#8a8a8a;
  --footer-bg:#1c1c1c;
  --footer-line:#3a3a3a;
  --logo-text:#2f3a33;
}
*{box-sizing:border-box;margin:0;padding:0}
html,body{width:1200px;height:2184px;overflow:hidden}
body{position:relative;font-family:"Roboto",sans-serif;color:var(--white);background:#222}
.backdrop{position:absolute;inset:0 0 91px 0;
  background:linear-gradient(180deg,#3d4536 0%,#2f332b 20%,#3a3326 45%,#2b2a25 70%,#1f1f1d 100%)}
.site-header{position:absolute;left:0;top:0;width:1200px;height:131px;
  background:linear-gradient(90deg,#e9ece6 0%,#d6dccf 25%,#6d7c55 45%,#4f5f38 70%,#3d4a2c 100%)}
.brand{position:absolute;left:90px;top:40px;display:flex;align-items:center;gap:8px;white-space:nowrap}
.brand-mark{width:44px;height:44px;border-radius:50%;border:4px solid var(--green-light);flex:none}
.brand-name{font-family:"Poppins",sans-serif;font-weight:600;font-size:22px;color:var(--logo-text)}
.main-nav{position:absolute;left:330px;top:48px;display:flex;gap:30px;font-family:"Poppins",sans-serif;font-size:17px;white-space:nowrap}
.main-nav a{color:var(--white);text-decoration:none}
.social{position:absolute;left:967px;top:45px;display:flex;gap:6px}
.social span{width:32px;height:32px;border-radius:50%;border:1.5px solid var(--white)}
.page-title{position:absolute;top:206px;left:0;width:1200px;text-align:center;font-family:"Poppins",sans-serif;font-weight:500;font-size:44px}
.intro{position:absolute;top:275px;left:150px;width:900px;text-align:center;font-size:16px;line-height:32px;color:var(--text-light)}
.form-frame{position:absolute;left:92px;top:425px;width:1019px;height:1528px;border:1px solid var(--frame)}
.row{position:absolute;left:0;width:100%;height:54px}
.row label,.row .label{position:absolute;right:612px;width:400px;text-align:right;font-size:17px;line-height:26px;color:var(--white);top:50%;transform:translateY(-50%)}
.field{position:absolute;left:448px;top:0;width:493px;height:54px;background:var(--input-bg);border:none;font-family:"Roboto",sans-serif;font-size:17px;color:var(--field-text);padding:0 16px;display:flex;align-items:center}
.field.ph{font-style:italic;font-size:15px;color:var(--placeholder)}
.field.select::after{content:"";position:absolute;right:16px;top:24px;border:6px solid transparent;border-top:7px solid #555;border-bottom:0}
.field.half{width:241px}
.field.half.second{left:700px}
.field svg{position:absolute;right:14px;top:17px}
.choices{position:absolute;left:448px;top:50%;transform:translateY(-50%);display:flex;gap:36px;font-size:17px}
.choice{display:flex;align-items:center;gap:7px}
.radio{width:16px;height:16px;border-radius:50%;border:1.5px solid #ccc;position:relative}
.radio.on::after{content:"";position:absolute;left:2.5px;top:2.5px;width:8px;height:8px;border-radius:50%;background:var(--green-light)}
.submit{position:absolute;left:425px;top:1423px;width:167px;height:46px;border-radius:23px;background:var(--green);color:var(--white);font-family:"Poppins",sans-serif;font-size:22px;font-weight:500;display:flex;align-items:center;justify-content:center}
.site-footer{position:absolute;left:0;top:2093px;width:1200px;height:91px;background:var(--footer-bg);border-top:1px solid var(--footer-line);text-align:center;font-size:17px;line-height:91px;color:var(--text-light)}
</style>
</head>
<body>
<div class="backdrop" role="img" aria-label="Photo of a waste collection truck parked under trees, darkened"></div>

<header class="site-header" role="img" aria-label="Photo of green tree canopy">
  <div class="brand"><span class="brand-mark"></span><span class="brand-name">Tolvin Waste</span></div>
  <nav class="main-nav"><a href="#">About us</a><a href="#">What we do</a><a href="#">Resources</a><a href="#">Contact us</a></nav>
  <div class="social"><span></span><span></span><span></span><span></span></div>
</header>

<h1 class="page-title">Waste Transporters</h1>
<p class="intro">Waste transporters and controlled waste carriers provide a vital link between waste producers and waste facilities. The safe transport of waste is an essential economic and community service. By registering your waste transportation services with Tolvin Waste your business will be visible to waste producers looking for waste transport options.</p>

<form class="form-frame">
  <div class="row" style="top:58px"><label>Registered business name</label><div class="field"></div></div>
  <div class="row" style="top:130px"><label>Trading as (if applicable)</label><div class="field"></div></div>
  <div class="row" style="top:203px"><label>Business address</label><div class="field"></div></div>
  <div class="row" style="top:275px"><label>Post code</label><div class="field"></div></div>
  <div class="row" style="top:348px"><label>Email contact</label><div class="field"></div></div>
  <div class="row" style="top:421px"><label>Phone contact</label><div class="field"></div></div>
  <div class="row" style="top:495px"><label>Regions of operation</label><div class="field select">Select</div></div>
  <div class="row" style="top:568px"><label>Days and times for collection</label>
    <div class="field half">Date<svg width="16" height="18" viewBox="0 0 16 18"><rect x="1" y="3" width="14" height="14" fill="none" stroke="#555" stroke-width="1.5"/><line x1="1" y1="7" x2="15" y2="7" stroke="#555" stroke-width="1.5"/><line x1="5" y1="1" x2="5" y2="4" stroke="#555" stroke-width="1.5"/><line x1="11" y1="1" x2="11" y2="4" stroke="#555" stroke-width="1.5"/></svg></div>
    <div class="field half second">Time<svg width="18" height="18" viewBox="0 0 18 18"><circle cx="9" cy="9" r="7.5" fill="none" stroke="#555" stroke-width="1.5"/><path d="M9 4.5V9l3 2" fill="none" stroke="#555" stroke-width="1.5"/></svg></div>
  </div>
  <div class="row" style="top:642px"><span class="label">Is the business registered as<br>a controlled waste carrier?</span>
    <div class="choices"><span class="choice"><span class="radio on"></span>Yes</span><span class="choice"><span class="radio"></span>No</span></div></div>
  <div class="row" style="top:712px"><label>Controlled waste carrier number</label><div class="field"></div></div>
  <div class="row" style="top:781px"><span class="label">Is the business a registered<br>as a Dangerous goods carrier?</span>
    <div class="choices"><span class="choice"><span class="radio on"></span>Yes</span><span class="choice"><span class="radio"></span>No</span></div></div>
  <div class="row" style="top:859px"><label>Dangerous goods number</label><div class="field"></div></div>
  <div class="row" style="top:932px"><label>Wastes accepted (codes)</label><div class="field select">Select Code</div></div>
  <div class="row" style="top:1005px"><label>Wastes accepted (description)</label><div class="field ph">Bulk liquid/packaged/solid wastes</div></div>
  <div class="row" style="top:1079px"><label>Minimum volume of waste collected</label><div class="field ph">Number/L or Number/kg or Number/m</div></div>
  <div class="row" style="top:1152px"><label>Maximum volume of waste collected</label><div class="field ph">Number/L or Number/kg or Number/m</div></div>
  <div class="row" style="top:1226px"><span class="label">Costs (for each type of waste collected<br>or all types of waste if the same cost for each)</span><div class="field ph">Dollars per kg, Litre, tonne, m3 per kilometre</div></div>
  <div class="row" style="top:1308px"><span class="label">Would you like Tolvin waste to advertise<br>your carrier services on this website?</span>
    <div class="choices"><span class="choice"><span class="radio on"></span>Yes</span><span class="choice"><span class="radio"></span>No</span></div></div>
  <div class="submit">Submit</div>
</form>

<footer class="site-footer">Copyright © 2018. All Rights Reserved</footer>
</body>
</html>
```